Concert Poster

Dear all!
It seems that we have found our final design!
Thanks a lot for your contribution so far. It is not necessary to post any more designs.

BR Lukas

____________________
For the band Velvet Comet - we would like to have a standard concert announcement poster that we can use to advertise for our gigs.The band plays the classic songs of the disco era end of the 70ies, e.g. Lumo, Carla Brightwood, Silver Moth Parade, Rudy & The Orbits etc. On stage we also adapt to the fashion of those times, but in a modern manner.See more details on our website: www.velvetcomet-band.de

We intend to position the band in the high price segment - so that poster should be positively effective even between posters of famous bands.

Format: DIN-A1 Portrait - 594 x 841 mm

If possible, it would also be great if we could use the same design to print flyers (format DIN-A6).

Target Market(s)

Live Music Bands

Requirements
Must have
• The poster should contain:
• - Our logo (see uploads)
• - Our official photo (see uploads)
• - Text about date, venue, time, entrance fee or the concert AND
• alternatively a possibility to leave this space blank so that we can print a bunch of empty posters that we can write the details on manually (to avoid printing posters for each gig individually)
• - Information about the Band:
• - Website: www.velvetcomet-band.de
• - Like us on facebook: fb/velvetcometband

```html
<!DOCTYPE html>
<html lang="en">
<head>
<meta charset="utf-8">
<title>Velvet Comet – Concert Poster</title>
<link rel="stylesheet" href="https://fonts.googleapis.com/css2?family=Montserrat:wght@400;500;700;800&display=swap">
<style>
  :root {
    --page-bg: #2a2a2d;
    --poster-dark: #0c0a10;
    --poster-plum: #3a0f35;
    --poster-magenta: #8e1a72;
    --glow-pink: #e0359f;
    --logo-tint: #ffd9f1;
    --text-light: #f4eef4;
    --text-muted: #d8c6d6;
  }
  * { box-sizing: border-box; margin: 0; padding: 0; }
  html, body { width: 1200px; height: 800px; overflow: hidden; }
  body {
    background: var(--page-bg);
    font-family: "Montserrat", Arial, sans-serif;
    display: flex;
    align-items: center;
    justify-content: center;
  }
  .poster {
    position: relative;
    width: 537px;
    height: 760px;
    overflow: hidden;
    background: linear-gradient(180deg, var(--poster-dark) 0%, var(--poster-dark) 38%, var(--poster-plum) 62%, var(--poster-magenta) 100%);
  }
  .band-photo {
    position: absolute;
    left: 60px;
    top: 22px;
    width: 420px;
    height: 300px;
    border-radius: 6px;
    background: radial-gradient(ellipse at 50% 45%, #6b4a3a 0%, #3a2a2c 45%, #140f15 80%);
  }
  .glow-shape {
    position: absolute;
    left: 0;
    top: 200px;
    width: 537px;
    height: 360px;
  }
  .disco-ball {
    position: absolute;
    left: 198px;
    top: 262px;
    width: 140px;
    height: 140px;
    border-radius: 50%;
    background: radial-gradient(circle at 40% 35%, #ffd0ee 0%, #e04aae 40%, #7d1563 100%);
  }
  .band-logo {
    position: absolute;
    left: 0;
    right: 0;
    top: 404px;
    text-align: center;
    font-weight: 800;
    font-size: 64px;
    line-height: 1;
    letter-spacing: 1px;
    color: var(--logo-tint);
    text-transform: uppercase;
  }
  .band-logo span { display: block; font-size: 52px; margin-top: 8px; }
  .gig-date {
    position: absolute;
    left: 0;
    right: 0;
    top: 602px;
    text-align: center;
    font-weight: 500;
    font-size: 30px;
    letter-spacing: 1px;
    color: var(--text-light);
  }
  .gig-details {
    position: absolute;
    left: 40px;
    right: 40px;
    top: 652px;
    display: flex;
    align-items: center;
    justify-content: space-between;
    color: var(--text-muted);
    font-size: 11px;
  }
  .venue-name {
    font-weight: 700;
    font-size: 22px;
    color: var(--text-light);
  }
  .band-links {
    position: absolute;
    left: 40px;
    right: 40px;
    bottom: 26px;
    display: flex;
    justify-content: space-between;
    font-size: 10px;
    color: var(--text-light);
  }
</style>
</head>
<body>
  <main class="poster">
    <div class="band-photo" role="img" aria-label="Official band photo: six members in colourful disco-era outfits around a mirror ball"></div>

    <svg class="glow-shape" viewBox="0 0 537 360" aria-hidden="true">
      <defs>
        <radialGradient id="pinkGlow" cx="50%" cy="45%" r="55%">
          <stop offset="0%" stop-color="#e0359f" stop-opacity="0.85"/>
          <stop offset="60%" stop-color="#b0227f" stop-opacity="0.5"/>
          <stop offset="100%" stop-color="#b0227f" stop-opacity="0"/>
        </radialGradient>
      </defs>
      <ellipse cx="268" cy="180" rx="250" ry="170" fill="url(#pinkGlow)"/>
    </svg>

    <div class="disco-ball" role="img" aria-label="Glowing pink mirror ball illustration"></div>

    <h1 class="band-logo">Velvet<span>Comet</span></h1>

    <p class="gig-date">25 DECEMBER 2018</p>

    <div class="gig-details">
      <span class="gig-start">start at 21:00</span>
      <span class="venue-name">Nocturne Club</span>
      <span class="gig-fee">entrance 15€</span>
    </div>

    <footer class="band-links">
      <span class="band-website">www.velvetcomet-band.de</span>
      <span class="band-social">fb/velvetcometband</span>
    </footer>
  </main>
</body>
</html>
```